Feral Tundra, a 3d voxel survival video game needs a card for gaming conventions

I am the lead developer for Feral Tundra http://www.FeralTundra.example and need a business card to hand out at an indie gaming convention
The card would need to include the game name, website url, my name, position (Lead Developer), e-mail and phone number
The game is a 3d, voxel (with smooth terrain) based survival game with guns and wildlife. The main icon of the game would likely be a grizzly bear but I am willing to accept other designs too.
Attached is a media kit for the game with some images you can use but don't have to its just what little art I can provide. Anything on the website or from the video game can also be used. unrelated art can also be used.
Target Market(s)
Indie Developers/publishers at conferences
Industry/Entity Type
Games
Contact Information for Business Card
Name: Corin Wexford
Position: Lead Developer
E-mail: Gray_Lanterns@mailnest.example
Phone number: 555-372-9186
Look and feel

```html
<!DOCTYPE html>
<html lang="en">
<head>
<meta charset="UTF-8">
<title>Feral Tundra — Business Card</title>
<link rel="stylesheet" href="https://fonts.googleapis.com/css2?family=Open+Sans:wght@400;600;800&display=swap">
<style>
  :root {
    --page-bg: #e9e7e4;
    --card-dark: #1d1d1e;
    --card-dark-edge: #2a2a2b;
    --divider: #3a3a3c;
    --brand-red: #b0281c;
    --brand-gold: #c9a24a;
    --text-light: #e6e6e6;
    --front-top: #a8170e;
    --front-mid: #b5553a;
    --front-bottom: #b9a45e;
    --bear-dark: #4a2a16;
    --bear-mid: #7a4526;
    --logo-olive: #4d5a2a;
  }
  * { box-sizing: border-box; margin: 0; padding: 0; }
  html, body {
    width: 1200px; height: 844px; overflow: hidden;
    background: var(--page-bg);
    font-family: "Open Sans", Arial, sans-serif;
  }
  .sheet {
    position: relative; width: 1200px; height: 844px;
    display: flex; align-items: center; justify-content: center; gap: 50px;
  }
  .card {
    position: relative; width: 525px; height: 300px;
    border-radius: 3px; overflow: hidden;
    box-shadow: 0 8px 22px rgba(0,0,0,.25);
  }

  /* Back side: contact details */
  .card--back {
    background: radial-gradient(circle at 30% 40%, var(--card-dark-edge), var(--card-dark) 70%);
  }
  .card--back .brand-name {
    position: absolute; left: 50px; top: 132px;
    font-weight: 800; font-size: 30px; letter-spacing: 2px; line-height: 1.05;
    color: var(--brand-red); text-transform: uppercase;
  }
  .card--back .divider {
    position: absolute; left: 262px; top: 62px; width: 1px; height: 200px;
    background: var(--divider);
  }
  .person {
    position: absolute; left: 276px; top: 66px;
  }
  .person__name {
    font-size: 15px; font-weight: 600; letter-spacing: .5px; text-transform: uppercase;
  }
  .person__first { color: var(--brand-red); }
  .person__last { color: var(--brand-gold); }
  .person__role { font-size: 12px; color: var(--text-light); margin-top: 1px; }
  .contacts {
    position: absolute; left: 286px; top: 170px; width: 215px; list-style: none;
    font-size: 11.5px; color: var(--text-light);
  }
  .contacts li { display: flex; align-items: center; gap: 7px; margin-bottom: 4px; white-space: nowrap; }
  .contacts svg { width: 10px; height: 10px; fill: var(--text-light); flex: none; }

  /* Front side: key art */
  .card--front {
    background: linear-gradient(160deg, var(--front-top) 0%, var(--front-mid) 50%, var(--front-bottom) 100%);
  }
  .key-art {
    position: absolute; left: 118px; top: 96px; width: 230px; height: 204px;
    border-radius: 48% 52% 0 0 / 40% 45% 0 0;
    background: radial-gradient(ellipse at 60% 35%, var(--bear-mid), var(--bear-dark) 75%);
  }
  .card--front .brand-name {
    position: absolute; left: 230px; top: 70px;
    font-weight: 800; font-size: 40px; letter-spacing: 3px; line-height: 1.05;
    color: var(--logo-olive); text-transform: uppercase;
  }
</style>
</head>
<body>
  <main class="sheet">
    <section class="card card--back" aria-label="Business card back">
      <p class="brand-name">Feral<br>Tundra</p>
      <span class="divider"></span>
      <div class="person">
        <p class="person__name"><span class="person__first">Corin</span> <span class="person__last">Wexford</span></p>
        <p class="person__role">Lead Developer</p>
      </div>
      <ul class="contacts">
        <li>
          <svg viewBox="0 0 24 24" aria-hidden="true"><path d="M6.6 10.8a15 15 0 0 0 6.6 6.6l2.2-2.2c.3-.3.7-.4 1-.2 1.1.4 2.3.6 3.6.6.6 0 1 .4 1 1V20c0 .6-.4 1-1 1A17 17 0 0 1 3 4c0-.6.4-1 1-1h3.5c.6 0 1 .4 1 1 0 1.3.2 2.5.6 3.6.1.3 0 .7-.2 1z"/></svg>
          555-372-9186
        </li>
        <li>
          <svg viewBox="0 0 24 24" aria-hidden="true"><path d="M2 5h20v14H2zm2 2v.5l8 5 8-5V7zm0 2.8V17h16V9.8l-8 5z"/></svg>
          Gray_Lanterns@mailnest.example
        </li>
        <li>
          <svg viewBox="0 0 24 24" aria-hidden="true"><path d="M12 2a10 10 0 1 0 0 20 10 10 0 0 0 0-20zm6.9 6h-2.9a15 15 0 0 0-1.4-3.6A8 8 0 0 1 18.9 8zM12 4c.8 1.2 1.5 2.5 1.9 4h-3.8c.4-1.5 1.1-2.8 1.9-4zM4.3 14a8 8 0 0 1 0-4h3.4a16 16 0 0 0 0 4zm.8 2h2.9c.3 1.3.8 2.5 1.4 3.6A8 8 0 0 1 5.1 16zM8 8H5.1a8 8 0 0 1 4.3-3.6C8.8 5.5 8.3 6.7 8 8zm4 12c-.8-1.2-1.5-2.5-1.9-4h3.8c-.4 1.5-1.1 2.8-1.9 4zm2.3-6H9.7a14 14 0 0 1 0-4h4.6a14 14 0 0 1 0 4zm.3 5.6c.6-1.1 1.1-2.3 1.4-3.6h2.9a8 8 0 0 1-4.3 3.6zm1.7-5.6a16 16 0 0 0 0-4h3.4a8 8 0 0 1 0 4z"/></svg>
          http://www.FeralTundra.example
        </li>
      </ul>
    </section>

    <section class="card card--front" aria-label="Business card front">
      <div class="key-art" role="img" aria-label="Photo of a roaring brown grizzly bear rising from the lower edge"></div>
      <p class="brand-name">Feral<br>Tundra</p>
    </section>
  </main>
</body>
</html>
```